Custom Manufacturing Job Shop

We are looking for a business card design for Tall Oak Fabrication Inc. Tall Oak is a family owned business that manufactures any custom product to fit a customers needs, whether it is custom 1 piece or production parts, we truly take on projects that others just cant do. to help in your design go to www.talloakfab.example for a more in depth idea. we have the following capabilities that we would like to see on the card somewhere...maybe on the back of a 2 sided card? we are fully open to ideas.
Machining
• Fabrication
• Millwork
• Maintenance
• Laser Cutting
• Precision Forming
Engineering
Blasting/Painting

No matter how big or small, We literally do it all

preferably black or darker cards but we don't mind to see some color if you see a better fit. we are interested in looking at anything that catches attention.
I have attached our logo, if it is needed in a different file type please let me know and I will send it to you if I can. maybe adding some type of drawing or dimensional lines would be something to add?? just throwing ideas out there....

Reason: I added one of our shredder designs and would like to see a few more cards if possible using this. any questions please don't hesitate to ask!!

Target Market(s)

anyone looking for design/manufacturing/machining whether it is custom 1 off parts or production.

Industry/Entity Type

Business

Contact Information for Business Card

preferably darker shades, but also not opposed to some color in the same sense....not too bright

Font styles to use
Serif
Sans Serif

Requirements
Must have
• Dell Marwick
• Direct:555-213-7790
• Cell:555-348-1162
• Fax: 555-907-4425
• 42 Quarry Lane
• Cedar Hollow, ST 00000
• I also would request having it in a format I can give to the company making the business cards to edit names/numbers etc. for the entire staff.
Nice to have
• drafting lines? we are open to almost anything....
Should not have
• exotic colors

```html
<!DOCTYPE html>
<html lang="en">
<head>
<meta charset="utf-8">
<title>Tall Oak Fabrication – Business Card</title>
<link rel="stylesheet" href="https://fonts.googleapis.com/css2?family=Cinzel:wght@400;700&display=swap">
<style>
  :root {
    --page-bg: #ffffff;
    --card-navy: #0f2b5c;
    --accent-green: #1e7d3c;
    --text-light: #e4e8ef;
    --brand-silver: #c8ced8;
    --brand-faint: #3a5584;
    --card-shadow: rgba(0, 0, 0, 0.22);
  }
  html, body {
    margin: 0;
    padding: 0;
    width: 1200px;
    height: 1200px;
    overflow: hidden;
    background: var(--page-bg);
  }
  .canvas {
    position: relative;
    width: 1200px;
    height: 1200px;
    font-family: "Cinzel", serif;
  }
  .card {
    position: absolute;
    left: 324px;
    width: 551px;
    height: 309px;
    background: var(--card-navy);
    box-shadow: 6px 7px 8px var(--card-shadow);
  }
  .card--front { top: 236px; }
  .card--back { top: 669px; }

  .brand {
    position: absolute;
    display: flex;
    align-items: center;
    gap: 10px;
    font-family: "Cinzel", serif;
    font-weight: 700;
    white-space: nowrap;
  }
  .card--front .brand {
    left: 48px;
    top: 50px;
    font-size: 38px;
    color: var(--brand-silver);
  }
  .brand__square {
    width: 14px;
    height: 14px;
    background: currentColor;
  }
  .card--back .brand {
    left: 0;
    right: 0;
    top: 88px;
    justify-content: center;
    font-size: 66px;
    color: var(--brand-faint);
  }

  .contact-name {
    position: absolute;
    left: 54px;
    top: 200px;
    margin: 0;
    font-size: 22px;
    font-weight: 400;
    letter-spacing: 1px;
    color: var(--accent-green);
  }
  .contact-address {
    position: absolute;
    left: 54px;
    top: 243px;
    margin: 0;
    font-style: normal;
    font-size: 12.5px;
    line-height: 22px;
    letter-spacing: 1.8px;
    color: var(--text-light);
  }
  .phone-list {
    position: absolute;
    left: 368px;
    top: 197px;
    margin: 0;
    padding: 0;
    list-style: none;
  }
  .phone-list li {
    display: flex;
    align-items: center;
    height: 27px;
    font-size: 11.5px;
    letter-spacing: 1.6px;
    color: var(--text-light);
  }
  .phone-list__label {
    display: inline-flex;
    align-items: center;
    justify-content: center;
    width: 18px;
    height: 18px;
    margin-right: 10px;
    background: var(--accent-green);
    color: #ffffff;
    font-size: 13px;
    letter-spacing: 0;
  }
  .website {
    position: absolute;
    left: 0;
    right: 0;
    top: 270px;
    margin: 0;
    text-align: center;
    font-size: 14px;
    font-weight: 700;
    letter-spacing: 0.8px;
    color: #ffffff;
  }
</style>
</head>
<body>
<main class="canvas">
  <section class="card card--front" aria-label="Business card front">
    <div class="brand"><span class="brand__square"></span>Tall Oak</div>
    <h1 class="contact-name">Dell Marwick</h1>
    <address class="contact-address">
      42 Quarry Lane<br>
      Cedar Hollow, ST 00000
    </address>
    <ul class="phone-list">
      <li><span class="phone-list__label">D</span>555-213-7790</li>
      <li><span class="phone-list__label">C</span>555-348-1162</li>
      <li><span class="phone-list__label">F</span>555-907-4425</li>
    </ul>
  </section>

  <section class="card card--back" aria-label="Business card back">
    <div class="brand">Tall Oak</div>
    <p class="website">WWW.TALLOAKFAB.EXAMPLE</p>
  </section>
</main>
</body>
</html>
```